Business Image

I have recently had a new company logo made up and require some new business cards to go with it.

Target Market(s)

Developers & high worth clients.

Industry/Entity Type

Business

Contact Information for Business Card

The business is in the construction/management industry. It needs to be classy but have a industrial feel. I would like the business card to be a elegant presentation in itself.

Requirements
Must have
• Current logo & company name. Colouring needs to be the same as the current design also.
Nice to have
• A few different designs & presentations of single and double sided business cards.

```html
<!DOCTYPE html>
<html lang="en">
<head>
<meta charset="utf-8">
<title>Ironvale Management Group – Business Cards</title>
<link href="https://fonts.googleapis.com/css2?family=Open+Sans:wght@400;600&display=swap" rel="stylesheet">
<style>
  :root {
    --backdrop: #3b3532;
    --card: #141516;
    --card-edge: #0c0c0d;
    --accent-blue: #2f6d9c;
    --brand-grey: #5a5d61;
    --text-white: #f2f2f2;
    --text-muted: #8a8c8f;
    --rule: #d9d9d9;
  }
  * { margin: 0; padding: 0; box-sizing: border-box; }
  html, body {
    width: 1200px;
    height: 864px;
    overflow: hidden;
    background: var(--backdrop);
    font-family: "Open Sans", Arial, sans-serif;
  }
  .canvas {
    position: relative;
    width: 1200px;
    height: 864px;
  }
  .card {
    position: absolute;
    width: 520px;
    height: 298px;
    background: var(--card);
    border-radius: 3px;
    box-shadow: 0 14px 30px rgba(0,0,0,0.45), 0 0 0 1px var(--card-edge);
  }
  /* Back of card */
  .card-back {
    left: 70px;
    top: 130px;
  }
  .back-brand {
    position: absolute;
    left: 0; right: 0;
    top: 92px;
    display: flex;
    align-items: center;
    justify-content: center;
    gap: 14px;
  }
  .back-brand .brand-square {
    width: 40px;
    height: 40px;
    background: #2a2b2d;
  }
  .back-brand .brand-name {
    font-size: 24px;
    font-weight: 600;
    color: #3a3c3f;
    letter-spacing: 1px;
  }
  .back-website {
    position: absolute;
    left: 0; right: 0;
    bottom: 66px;
    text-align: center;
    font-size: 12px;
    letter-spacing: 2.5px;
    color: var(--text-muted);
  }
  /* Front of card */
  .card-front {
    left: 610px;
    top: 420px;
  }
  .person {
    position: absolute;
    left: 30px;
    top: 58px;
  }
  .person-name {
    font-size: 12px;
    font-weight: 600;
    color: var(--accent-blue);
    letter-spacing: 0.5px;
    text-transform: uppercase;
  }
  .person-title {
    font-size: 14px;
    color: var(--text-white);
    margin-top: 2px;
  }
  .contact-list {
    position: absolute;
    left: 30px;
    top: 110px;
    list-style: none;
  }
  .contact-list li {
    display: flex;
    align-items: center;
    gap: 9px;
    font-size: 12.5px;
    color: var(--text-white);
    line-height: 19px;
  }
  .contact-list svg { width: 11px; height: 11px; fill: var(--brand-grey); }
  .divider {
    position: absolute;
    left: 30px;
    right: 30px;
    top: 172px;
    height: 1px;
    background: var(--rule);
  }
  .front-brand {
    position: absolute;
    right: 30px;
    top: 80px;
    display: flex;
    align-items: center;
    gap: 10px;
  }
  .front-brand .brand-square {
    width: 26px;
    height: 26px;
    background: var(--accent-blue);
  }
  .front-brand .brand-name {
    font-size: 17px;
    font-weight: 600;
    color: var(--accent-blue);
    letter-spacing: 0.5px;
  }
  .address {
    position: absolute;
    right: 30px;
    bottom: 28px;
    text-align: right;
    font-size: 13px;
    line-height: 18px;
    color: var(--text-white);
  }
</style>
</head>
<body>
<main class="canvas">

  <section class="card card-back" aria-label="Card back">
    <div class="back-brand">
      <span class="brand-square"></span>
      <span class="brand-name">Ironvale Management Group</span>
    </div>
    <p class="back-website">www.ironvalemanagementgroup.com</p>
  </section>

  <section class="card card-front" aria-label="Card front">
    <div class="person">
      <p class="person-name">Daniel Reyes</p>
      <p class="person-title">CEO/FOUNDER</p>
    </div>

    <ul class="contact-list">
      <li>
        <svg viewBox="0 0 12 12" aria-hidden="true"><path d="M1 4c0-1.5 2-3 5-3s5 1.5 5 3l-2 1-1-1.5H4L3 5 1 4zM2 6h8l1 5H1z"/></svg>
        555 210 4471
      </li>
      <li>
        <svg viewBox="0 0 12 12" aria-hidden="true"><path d="M3.5 0h5a1 1 0 0 1 1 1v10a1 1 0 0 1-1 1h-5a1 1 0 0 1-1-1V1a1 1 0 0 1 1-1zm.5 1.5v7.5h4V1.5z"/></svg>
        555 382 9016
      </li>
      <li>
        <svg viewBox="0 0 12 12" aria-hidden="true"><path d="M0 2h12v8H0zM1 3v.4l5 3.3 5-3.3V3z"/></svg>
        daniel@ironvale.com
      </li>
    </ul>

    <div class="front-brand">
      <span class="brand-square"></span>
      <span class="brand-name">Ironvale Management Group</span>
    </div>

    <div class="divider"></div>

    <address class="address" style="font-style:normal">
      2140 Cedar Bluff Road<br>
      Fairbanks, Alaska 99701<br>
      www.ironvale.com
    </address>
  </section>

</main>
</body>
</html>
```